Business Cards for Harbourline Coatings Pty Ltd

Hi every one i need a design for my buisness cards. I Want my logo in it and the name of the company needs to stand out Harbourline Coatings Pty Ltd. I want the background of the buisness cards black and i want the font to stand out in either a white or a silver stylish text. I want the design to be simple but original not to in your face if you know what i mean. I want on the back of the buisness cards to have the services that my buisness offers.
• Interior/Exterior
• Residential/Commercial
• Special effects/Texture Coatings
• Water Damage Repair
• Fully qualified
• Pensioner Discount
• 10 Year guarantee
• Fully Insured
• Obligation free quotes
full internal repaints include a proffesionla cleaning service
I want the services on the back to be layed out in an originall way not just dot points. If possible could my logo take up the whole back ground of the back but the text with the services be kind of like transparent so u cvan still see the logo i dont know if its possible it woiuld just look cool if possible. When i pick a design ill give my contact details to the designer to add to the design at the end. Any questions please just ask! Ill upload my logo.
Conatcs will include office phone: Mobile: E-mail - dale@harbourlinecoatings.com.au, Ill also have a Postal address which is a PO Box and my website is www.harbourlinecoatings.com.au

```html
<!DOCTYPE html>
<html lang="en">
<head>
<meta charset="utf-8">
<title>Harbourline Coatings Pty Ltd – Business Cards</title>
<link rel="stylesheet" href="https://fonts.googleapis.com/css2?family=Montserrat:wght@600&family=Open+Sans:wght@400&display=swap">
<style>
  :root {
    --backdrop: #3b352f;
    --card-black: #050505;
    --frame-line: #9a9a9a;
    --silver: #d4d4d4;
    --silver-soft: rgba(212, 212, 212, 0.72);
    --contact-white: #ffffff;
    --glow: #4a4a4a;
    --mark-grey: #1c1c1c;
  }
  * { margin: 0; padding: 0; box-sizing: border-box; }
  html, body {
    width: 1200px;
    height: 705px;
    overflow: hidden;
    background: var(--backdrop);
  }
  .card-sheet {
    position: relative;
    width: 1200px;
    height: 705px;
  }
  .card {
    position: absolute;
    top: 198px;
    width: 540px;
    height: 309px;
    background: var(--card-black);
    overflow: hidden;
  }
  .card--front { left: 40px; }
  .card--back { left: 620px; }

  .card__frame {
    position: absolute;
    inset: 0;
    width: 100%;
    height: 100%;
  }

  /* Front */
  .brand-mark {
    position: absolute;
    top: 26px;
    left: 0;
    right: 0;
    display: flex;
    justify-content: center;
    align-items: center;
    gap: 10px;
  }
  .brand-mark__square {
    width: 56px;
    height: 56px;
    background: var(--silver);
  }
  .brand-mark__name {
    font-family: "Montserrat", sans-serif;
    font-weight: 600;
    font-size: 15px;
    letter-spacing: 1px;
    color: var(--silver);
  }
  .company {
    position: absolute;
    top: 160px;
    left: 0;
    right: 0;
    display: flex;
    justify-content: center;
  }
  .company__block {
    display: flex;
    flex-direction: column;
    align-items: flex-end;
  }
  .company__name {
    font-family: "Montserrat", sans-serif;
    font-weight: 600;
    font-size: 27px;
    letter-spacing: 0.5px;
    color: var(--silver);
    line-height: 1.1;
  }
  .company__suffix {
    font-family: "Montserrat", sans-serif;
    font-weight: 600;
    font-size: 16px;
    color: var(--silver);
    margin-top: 4px;
  }

  /* Back */
  .back-glow {
    position: absolute;
    left: 90px;
    top: -60px;
    width: 360px;
    height: 200px;
    background: radial-gradient(ellipse at center, var(--glow) 0%, rgba(40,40,40,0.4) 45%, rgba(5,5,5,0) 75%);
  }
  .back-mark {
    position: absolute;
    left: 155px;
    top: 70px;
    width: 230px;
    height: 230px;
    border-radius: 50%;
    background: var(--mark-grey);
    opacity: 0.7;
  }
  .services {
    position: absolute;
    left: 0;
    right: 0;
    top: 34px;
    list-style: none;
    text-align: center;
    font-family: "Open Sans", sans-serif;
    font-size: 12px;
    line-height: 19px;
    letter-spacing: 0.3px;
    color: var(--silver-soft);
  }
  .services__note {
    font-size: 11px;
    margin-top: 3px;
  }
  .contact {
    position: absolute;
    left: 0;
    right: 0;
    top: 176px;
    list-style: none;
    text-align: center;
    font-family: "Open Sans", sans-serif;
    font-size: 20px;
    line-height: 27px;
    color: var(--contact-white);
  }
</style>
</head>
<body>
<main class="card-sheet">

  <section class="card card--front" aria-label="Business card front">
    <svg class="card__frame" viewBox="0 0 540 309" aria-hidden="true">
      <g fill="none" stroke="var(--frame-line)" stroke-width="1">
        <rect x="9.5" y="9.5" width="521" height="290"/>
        <rect x="14.5" y="14.5" width="511" height="280"/>
        <rect x="9.5" y="9.5" width="9" height="9"/>
        <rect x="521.5" y="9.5" width="9" height="9"/>
        <rect x="9.5" y="290.5" width="9" height="9"/>
        <rect x="521.5" y="290.5" width="9" height="9"/>
      </g>
    </svg>
    <div class="brand-mark">
      <span class="brand-mark__square"></span>
      <span class="brand-mark__name">HARBOURLINE</span>
    </div>
    <div class="company">
      <div class="company__block">
        <h1 class="company__name">HARBOURLINE COATINGS</h1>
        <p class="company__suffix">PTY LTD</p>
      </div>
    </div>
  </section>

  <section class="card card--back" aria-label="Business card back">
    <div class="back-glow"></div>
    <div class="back-mark"></div>
    <svg class="card__frame" viewBox="0 0 540 309" aria-hidden="true">
      <g fill="none" stroke="var(--frame-line)" stroke-width="1">
        <rect x="9.5" y="9.5" width="521" height="290"/>
        <rect x="14.5" y="14.5" width="511" height="280"/>
        <rect x="9.5" y="9.5" width="9" height="9"/>
        <rect x="521.5" y="9.5" width="9" height="9"/>
        <rect x="9.5" y="290.5" width="9" height="9"/>
        <rect x="521.5" y="290.5" width="9" height="9"/>
      </g>
    </svg>
    <ul class="services" aria-label="Services">
      <li>Interior / Exterior &nbsp;·&nbsp; Residential / Commercial</li>
      <li>Special Effects / Texture Coatings &nbsp;·&nbsp; Water Damage Repair</li>
      <li>Fully Qualified &nbsp;·&nbsp; Fully Insured &nbsp;·&nbsp; 10 Year Guarantee</li>
      <li>Pensioner Discount &nbsp;·&nbsp; Obligation Free Quotes</li>
      <li class="services__note">Full internal repaints include a professional cleaning service</li>
    </ul>
    <ul class="contact">
      <li>Office:(02) 5550 1827</li>
      <li>Mobile: 0400 555 318</li>
      <li>www.harbourlinecoatings.com.au</li>
      <li>E-mail: dale@harbourlinecoatings.com.au</li>
    </ul>
  </section>

</main>
</body>
</html>
```